Business Card Design

I need a business card designed for my new company BrightOak Home developments I specialise in all aspects of carpentry including Decks, Pergolas, Conventional Framing and fit outs I am open to different colours as long as it fits with my logo.

Industry/Entity Type

Carpentry

Contact Information for Business Card

BrightOak Home Developments, Greg Mollory, 0461802394, specialising in all aspects of carpentry and construction

```html
<!DOCTYPE html>
<html lang="en">
<head>
<meta charset="utf-8">
<title>BrightOak Home Developments – Business Card</title>
<link href="https://fonts.googleapis.com/css2?family=Ubuntu:ital,wght@0,400;0,500;0,700;1,700&display=swap" rel="stylesheet">
<style>
  :root {
    --brand-blue: #2b4f8f;
    --paper: #f7f7f7;
    --backdrop: #ececec;
    --shadow: rgba(0, 0, 0, 0.12);
  }
  * { box-sizing: border-box; margin: 0; padding: 0; }
  html, body {
    width: 1200px;
    height: 952px;
    overflow: hidden;
    background: var(--backdrop);
    font-family: "Ubuntu", Arial, sans-serif;
    color: var(--brand-blue);
  }
  .canvas {
    position: relative;
    width: 1200px;
    height: 952px;
  }
  .card {
    position: absolute;
    top: 328px;
    width: 520px;
    height: 297px;
    background: var(--paper);
    border-bottom: 6px solid var(--brand-blue);
    box-shadow: 0 6px 18px var(--shadow);
    overflow: hidden;
  }
  .card--front { left: 50px; }
  .card--back { left: 630px; }

  .wordmark {
    display: flex;
    align-items: center;
    gap: 10px;
    font-weight: 500;
    color: var(--brand-blue);
  }
  .wordmark__square {
    flex: none;
    background: var(--brand-blue);
  }
  .wordmark__name {
    line-height: 1.15;
    text-transform: uppercase;
    letter-spacing: 0.06em;
  }

  .card--front .wordmark {
    position: absolute;
    left: 0;
    right: 0;
    top: 110px;
    justify-content: center;
  }
  .card--front .wordmark__square { width: 22px; height: 22px; }
  .card--front .wordmark__name { font-size: 26px; }

  .card--back .wordmark {
    position: absolute;
    left: 28px;
    top: 34px;
  }
  .card--back .wordmark__square { width: 12px; height: 12px; }
  .card--back .wordmark__name { font-size: 14px; }

  .contact {
    position: absolute;
    right: 0;
    top: 112px;
    width: 210px;
  }
  .contact__name {
    display: block;
    background: var(--brand-blue);
    color: #ffffff;
    font-weight: 700;
    font-size: 16px;
    padding: 8px 0 8px 32px;
    border-radius: 18px 0 0 18px;
  }
  .contact__phone {
    display: flex;
    align-items: center;
    gap: 8px;
    margin-top: 8px;
    padding-left: 30px;
    font-size: 15px;
  }
  .contact__phone svg { width: 14px; height: 14px; fill: var(--brand-blue); }

  .specialty {
    position: absolute;
    left: 40px;
    top: 190px;
    width: 300px;
    text-align: center;
  }
  .specialty__label {
    font-weight: 700;
    font-style: italic;
    font-size: 15px;
  }
  .specialty__text {
    font-size: 15px;
    margin-top: 2px;
  }
</style>
</head>
<body>
  <main class="canvas">
    <section class="card card--front" aria-label="Business card front">
      <div class="wordmark">
        <span class="wordmark__square"></span>
        <span class="wordmark__name">BrightOak Home Developments</span>
      </div>
    </section>

    <section class="card card--back" aria-label="Business card back">
      <div class="wordmark">
        <span class="wordmark__square"></span>
        <span class="wordmark__name">BrightOak Home Developments</span>
      </div>

      <div class="contact">
        <span class="contact__name">Greg Mollory</span>
        <span class="contact__phone">046-180-2394
          <svg viewBox="0 0 24 24" aria-hidden="true"><path d="M6.6 10.8a15.1 15.1 0 0 0 6.6 6.6l2.2-2.2a1 1 0 0 1 1-.25 11.4 11.4 0 0 0 3.6.57 1 1 0 0 1 1 1V20a1 1 0 0 1-1 1A17 17 0 0 1 3 4a1 1 0 0 1 1-1h3.5a1 1 0 0 1 1 1c0 1.25.2 2.45.57 3.57a1 1 0 0 1-.25 1z"/></svg>
        </span>
      </div>

      <div class="specialty">
        <p class="specialty__label">Specialising in :</p>
        <p class="specialty__text">All aspects of carpentry &amp; construction</p>
      </div>
    </section>
  </main>
</body>
</html>
```